WordPress website in children books redesign

We are personalised children storybook creators with a range of personalized books, music CDs and DVDs that are created for each child. We sell our concept through a license via distributors / entrepreneurs mainly based in France and Europe. We want to focus on selling B2C to parents and grandparents, looking to buy presents to their children aged 0 to 10 years old. Those present are educative, unique for each child, and they will learn to have fun and learn to have fun. I would like to redesign our WordPress website https://pebblelanternkids.co.uk/index.php We are a children in the world of books and music books: books, music CDs and DVDs looking for something a little more along the lines of our competitors. See ike www.quillotop.com, www.tavirosa.com, www.lecheminduvelours.com, https://www.lespetitsbrume.com/, https://tinselpaths.com/ Our current website is a bit too old fashioned so I am looking at a much more modern design Here is a link for a few products that are not available here: https://www.filecrate.example/sh/kq417dzopfrnwtb/BXPL3rYmOk2u-sVH4dQkLN-zb?dl=0 We have 2 sides in our website: B2C on the left side and B2B on the right site; B2B is for distributors that are entrepreneurs buying our concept. for the homepage design, the main focus will be B2Consumer Our current page is too blended, lacks reassurance elements and I would like to have a look at this page. from our current stories. here is a link for our business book to give you a feel for it: http://online.pagewavo.com/qtlk/pzme/ MAIN PAGES TO REVIEW / HOMEPAGE / https://pebblelanternkids.co.uk/ BOOKS: https : //pebblelanternkids.co.uk/product-category/personalised-books/ MUSIC: https://pebblelanternkids.co.uk/product-category/music-cds/ BLOG: https://pebblelanternkids.co.uk/blog -2 / Looking forward to seeing you and your questions asap

Target Market(s)

parents and grandparents of children aged 0 to 10 years old. This is for the European market

Industry/Entity Type

Publishing Company

Number of Pages Required

4 page

Colors
0392cd
9bcb3b
ec1f27
757575

Requirements
Must have
• keep within the color code of our RGB logo: D25028 RGB: 8CC364 329BC8 808285
Nice to have
• be more with the style of our competitors. Pebble Lantern Kids am about making children learn the fun way, and develop their morality, self-esteem and confidence. It's about the magic of reading to help children learn while having fun. I have attached visuals but those are just examples and you we encourage you to suggest other ideas

```html
<!DOCTYPE html>
<html lang="en">
<head>
<meta charset="utf-8">
<title>Pebble Lantern Kids — Personalised Books</title>
<link rel="stylesheet" href="https://fonts.googleapis.com/css2?family=Montserrat:wght@400;600;700;800&family=Open+Sans:ital,wght@0,400;0,600;0,700;1,400&display=swap">
<style>
:root{
  --blue:#0392cd;
  --blue-deep:#1a78bd;
  --blue-dark:#0f5f9a;
  --green:#9bcb3b;
  --green-bg:#8cc23f;
  --red:#ec1f27;
  --orange:#d25028;
  --grey:#757575;
  --grey-light:#f0f0f0;
  --ink:#3a3a3a;
  --white:#ffffff;
  --head:"Montserrat",sans-serif;
  --body:"Open Sans",sans-serif;
}
*{box-sizing:border-box;margin:0;padding:0}
html,body{width:1200px;height:4544px;overflow:hidden}
body{position:relative;background:var(--white);font-family:var(--body);color:var(--grey)}
.abs{position:absolute}
a{color:inherit;text-decoration:none}

/* header */
.site-header{position:absolute;top:0;left:0;width:1200px;height:64px;background:var(--white);z-index:5}
.account-links{position:absolute;left:40px;top:12px;display:flex;gap:8px}
.account-links a{font:700 10px var(--head);letter-spacing:1px;padding:5px 10px;border:1.5px solid var(--red);color:var(--red);border-radius:3px}
.account-links a.login{border-color:var(--grey);color:var(--grey)}
.main-nav{position:absolute;top:40px;left:0;width:1200px;font:600 14px var(--head);color:var(--ink)}
.main-nav a{position:absolute}
.brand{position:absolute;left:520px;top:4px;width:160px;height:88px;background:var(--white);border-radius:0 0 80px 80px;display:flex;flex-direction:column;align-items:center;justify-content:center;gap:6px;z-index:6}
.brand-dot{width:28px;height:28px;border-radius:50%;background:var(--blue)}
.brand-name{font:700 14px var(--head);color:var(--blue);text-align:center;line-height:1.15}
.cart{position:absolute;right:40px;top:14px;display:flex;align-items:center;gap:10px;font:600 11px var(--head);color:var(--ink)}

/* hero */
.hero{position:absolute;top:64px;left:0;width:1200px;height:656px;background:linear-gradient(100deg,#e9ddcb 0%,#f6efe4 40%,#efe2d2 70%,#d9c2a7 100%)}
.hero-wave{position:absolute;left:0;top:560px;width:1200px;height:200px}
.hero-bubble{position:absolute;left:220px;top:372px;width:320px;height:166px;background:var(--white);border:4px solid var(--blue);border-radius:28px;display:flex;align-items:center;justify-content:center;text-align:center;font:800 26px/1.25 var(--head);color:var(--blue)}
.hero-bubble em{font-style:normal;color:var(--red)}

/* badges */
.badge{position:absolute;top:600px;width:280px;height:420px;z-index:3}
.badge-disc{position:absolute;left:0;top:0;width:280px;height:280px;border-radius:50%;box-shadow:0 6px 14px rgba(0,0,0,.18)}
.badge-ring{position:absolute;left:12px;top:12px;width:256px;height:256px;border-radius:50%;border:3px dashed rgba(255,255,255,.85)}
.badge-title{position:absolute;left:0;top:52px;width:280px;text-align:center;font:800 17px/1.25 var(--head);color:var(--white)}
.badge-art{position:absolute;left:80px;top:118px;width:120px;height:110px;border-radius:6px}
.badge-ribbon{position:absolute;left:70px;top:250px;width:140px;height:110px}
.blue-badge .badge-disc{background:var(--blue)}
.green-badge .badge-disc{background:var(--green)}
.red-badge .badge-disc{background:var(--red)}

/* characters */
.section-title{font:800 30px/1.3 var(--head);color:var(--blue);text-align:center}
.section-title .green{color:var(--green)}
.characters{position:absolute;top:1090px;left:0;width:1200px}
.character{position:absolute;top:110px;width:200px;text-align:center}
.character-art{width:120px;height:110px;margin:0 auto 18px;border-radius:50%}
.character h3{font:700 13px var(--head);color:var(--ink);letter-spacing:.5px;margin-bottom:8px}
.character p{font:400 11px/1.55 var(--body)}

/* best sellers */
.best-sellers{position:absolute;top:1480px;left:0;width:1200px;height:530px;background:var(--grey-light)}
.best-sellers .section-title{margin-top:36px}
.card-row{position:absolute;top:124px;left:180px;display:flex;gap:16px}
.product-card{width:196px;height:360px;background:var(--white);border-radius:4px;box-shadow:0 2px 8px rgba(0,0,0,.08);padding:14px;text-align:center}
.product-cover{width:168px;height:220px;border-radius:3px;margin-bottom:16px}
.price{font:700 15px var(--head);color:var(--red);text-align:left}
.product-name{font:400 12px var(--body);text-align:left;margin:6px 0 14px}
.buy{display:inline-block;font:600 11px var(--head);color:var(--blue);border:1.5px solid var(--blue);border-radius:14px;padding:5px 20px}

/* adventure */
.adventure{position:absolute;top:2010px;left:0;width:1200px;height:520px;background:var(--green-bg)}
.adventure-art{position:absolute;left:140px;top:100px;width:420px;height:320px;border-radius:6px;background:linear-gradient(135deg,#4d8d3a,#8fb65a 45%,#c9a470 100%);transform:rotate(-3deg)}
.adventure-copy{position:absolute;left:652px;top:170px;width:380px;color:var(--white)}
.adventure-copy h2{font:800 28px var(--head);margin-bottom:14px}
.adventure-copy p{font:400 12px/1.7 var(--body);margin-bottom:24px}
.btn{display:inline-block;font:700 11px var(--head);letter-spacing:1px;color:var(--white);padding:10px 26px;border-radius:20px}
.btn-blue{background:var(--blue)}
.btn-red{background:var(--red)}

/* personalisation */
.learning{position:absolute;top:2530px;left:0;width:1200px;height:640px;background:#fbfbfb}
.learning .section-title{margin-top:50px}
.learning-text{width:640px;margin:18px auto 0;text-align:center;font:400 12px/1.7 var(--body)}
.video{position:absolute;left:272px;top:250px;width:656px;height:360px;border-radius:4px;background:linear-gradient(120deg,#3a2c24,#7a5a45 50%,#2f2620)}
.play{position:absolute;left:298px;top:150px;width:60px;height:60px}

/* gallery */
.gallery{position:absolute;top:3170px;left:0;width:1200px;height:700px}
.gallery .section-title{margin-top:52px}
.gallery-grid{position:absolute;left:172px;top:230px;width:856px;height:360px;display:grid;grid-template-columns:1fr 1.5fr 1.5fr 1fr;grid-template-rows:1fr 1fr;gap:6px}
.tile{border-radius:2px}
.tile.tall{grid-row:span 2}
.gallery-more{position:absolute;top:622px;left:0;width:1200px;text-align:center}

/* testimonial */
.testimonial{position:absolute;left:180px;top:3880px;width:780px;height:180px;border:2px solid #dedede;border-radius:80px;background:var(--white);text-align:center;padding:34px 80px}
.testimonial p{font:italic 400 12px/1.7 var(--body)}
.quote{font:800 40px/0 var(--head);color:var(--blue);vertical-align:-14px}
.testimonial .author{font:700 14px var(--head);color:var(--red);margin-top:14px;font-style:normal}
.dragon{position:absolute;left:990px;top:3880px;width:130px;height:170px;border-radius:40% 40% 30% 30%;background:linear-gradient(160deg,#b67ac4,#8a58a3)}

/* footer */
.footer-stripes{position:absolute;left:0;top:4040px;width:1200px;height:80px}
.site-footer{position:absolute;top:4100px;left:0;width:1200px;height:444px;background:var(--blue-deep);color:var(--white)}
.footer-col{position:absolute;top:70px}
.footer-col h4{font:700 14px var(--head);margin-bottom:18px}
.footer-col li{list-style:none;font:400 11px/2 var(--body);opacity:.9}
.contact-line{display:flex;align-items:flex-start;gap:10px;font:400 11px/1.5 var(--body);margin-bottom:12px}
.socials{display:flex;gap:8px;margin-top:10px}
.socials span{width:24px;height:24px;border-radius:50%;border:1.5px solid var(--white)}
.footer-brand{position:absolute;left:950px;top:60px;width:150px;height:150px;background:var(--white);border-radius:8px;display:flex;flex-direction:column;align-items:center;justify-content:center;gap:8px}
.footer-brand .brand-name{width:110px}
.footer-bar{position:absolute;left:0;bottom:0;width:1200px;height:44px;background:var(--blue-dark);font:400 10px/44px var(--body);text-align:center;opacity:.95}
</style>
</head>
<body>

<header class="site-header">
  <div class="account-links"><a href="#">REGISTER</a><a href="#" class="login">LOGIN</a></div>
  <nav class="main-nav">
    <a href="#" style="left:172px">Welcome</a>
    <a href="#" style="left:262px">Our Products</a>
    <a href="#" style="left:400px">About Us</a>
    <a href="#" style="left:720px">Distributors</a>
    <a href="#" style="left:850px">Blog</a>
    <a href="#" style="left:920px">Contact Us</a>
    <a href="#" style="left:1016px">
      <svg width="14" height="14" viewBox="0 0 14 14"><circle cx="6" cy="6" r="4.5" fill="none" stroke="#3a3a3a" stroke-width="1.8"/><line x1="9.5" y1="9.5" x2="13" y2="13" stroke="#3a3a3a" stroke-width="1.8"/></svg>
    </a>
  </nav>
  <div class="cart">
    <svg width="14" height="14" viewBox="0 0 14 14"><circle cx="7" cy="4.5" r="3" fill="none" stroke="#757575" stroke-width="1.5"/><path d="M1.5 13c0-3 2.5-5 5.5-5s5.5 2 5.5 5" fill="none" stroke="#757575" stroke-width="1.5"/></svg>
    <svg width="16" height="14" viewBox="0 0 16 14"><path d="M1 1h2.5l2 8h8l1.5-6H4.5" fill="none" stroke="#ec1f27" stroke-width="1.5"/><circle cx="6.5" cy="12" r="1.2" fill="#ec1f27"/><circle cx="12" cy="12" r="1.2" fill="#ec1f27"/></svg>
    <span>(0 items)</span>
  </div>
</header>
<div class="brand"><span class="brand-dot"></span><span class="brand-name">Pebble Lantern Kids</span></div>

<section class="hero" role="img" aria-label="Photograph of a mother and young daughter reading a personalised storybook together in a bright living room">
  <svg class="hero-wave" viewBox="0 0 1200 200" preserveAspectRatio="none"><path d="M0 90 Q300 30 600 70 T1200 60 V200 H0 Z" fill="#ffffff"/></svg>
</section>
<div class="hero-bubble"><div>When children<br><em>become the heroes</em><br>of their own stories</div></div>

<div class="badge blue-badge" style="left:240px">
  <div class="badge-disc"></div><div class="badge-ring"></div>
  <div class="badge-title">Just Landed<br>Da reel Christmas</div>
  <div class="badge-art" role="img" aria-label="Christmas storybook cover" style="background:linear-gradient(135deg,#f3c24c,#d8452f)"></div>
  <svg class="badge-ribbon" viewBox="0 0 140 110"><path d="M20 0h100v110l-50-28-50 28z" fill="#0a6fa0"/></svg>
</div>
<div class="badge green-badge" style="left:460px">
  <div class="badge-disc"></div><div class="badge-ring"></div>
  <div class="badge-title">Bestseller<br>Music CDs</div>
  <div class="badge-art" role="img" aria-label="Music CD case artwork" style="background:linear-gradient(135deg,#f7e36a,#3aa0d8)"></div>
  <svg class="badge-ribbon" viewBox="0 0 140 110"><path d="M20 0h100v110l-50-28-50 28z" fill="#6f9a22"/></svg>
</div>
<div class="badge red-badge" style="left:680px">
  <div class="badge-disc"></div><div class="badge-ring"></div>
  <div class="badge-title">Most popular<br>Cartoon DVDs</div>
  <div class="badge-art" role="img" aria-label="Cartoon DVD case artwork" style="background:linear-gradient(135deg,#7fcff2,#2f6fb3)"></div>
  <svg class="badge-ribbon" viewBox="0 0 140 110"><path d="M20 0h100v110l-50-28-50 28z" fill="#b3141a"/></svg>
</div>

<section class="characters">
  <h2 class="section-title">Beautiful books about<br><span class="green">the children you love</span></h2>
  <div class="character" style="left:165px">
    <div class="character-art" role="img" aria-label="Illustrated purple dragon character" style="background:#b98ad0"></div>
    <h3>TED DOEUSM</h3>
    <p>Lorem ipsum dolor sit amet consectetur adipiscing elit sed do eiusmod tempor incididunt ut labore et dolore</p>
  </div>
  <div class="character" style="left:500px">
    <div class="character-art" role="img" aria-label="Illustrated yellow dog character" style="background:#f0c35a"></div>
    <h3>TED DOEUSM</h3>
    <p>Lorem ipsum dolor sit amet consectetur adipiscing elit sed do eiusmod tempor incididunt ut labore et dolore</p>
  </div>
  <div class="character" style="left:755px">
    <div class="character-art" role="img" aria-label="Illustrated brown hen character" style="background:#c98a55"></div>
    <h3>TED DOEUSM</h3>
    <p>Lorem ipsum dolor sit amet consectetur adipiscing elit sed do eiusmod tempor incididunt ut labore et dolore</p>
  </div>
</section>

<section class="best-sellers">
  <h2 class="section-title">More best-selling <span class="green">personalized books</span></h2>
  <div class="card-row">
    <article class="product-card">
      <div class="product-cover" role="img" aria-label="Storybook cover with a magical forest adventure" style="background:linear-gradient(160deg,#f2a43a,#c0392b)"></div>
      <div class="price">£ 24.00</div><div class="product-name">Dragon mysterious</div><a class="buy" href="#">Buy Now</a>
    </article>
    <article class="product-card">
      <div class="product-cover" role="img" aria-label="Storybook cover with children on a seaside journey" style="background:linear-gradient(160deg,#5bc1e8,#e9c04f)"></div>
      <div class="price">£ 24.00</div><div class="product-name">Dragon mysterious</div><a class="buy" href="#">Buy Now</a>
    </article>
    <article class="product-card">
      <div class="product-cover" role="img" aria-label="Christmas storybook cover" style="background:linear-gradient(160deg,#d8332e,#f0c24a)"></div>
      <div class="price">£ 24.00</div><div class="product-name">Dragon mysterious</div><a class="buy" href="#">Buy Now</a>
    </article>
    <article class="product-card">
      <div class="product-cover" role="img" aria-label="Storybook cover with a green dragon" style="background:linear-gradient(160deg,#3d7fc1,#6bbf4a)"></div>
      <div class="price">£ 24.00</div><div class="product-name">Dragon mysterious</div><a class="buy" href="#">Buy Now</a>
    </article>
  </div>
</section>

<section class="adventure">
  <div class="adventure-art" role="img" aria-label="Open storybook showing an illustrated woodland scene"></div>
  <div class="adventure-copy">
    <h2>Our brand new adventure</h2>
    <p>Lorem ipsum dolor sit amet, consectetur adipiscing elit, sed do eiusmod tempor incididunt ut labore et dolore magna aliqua. Ut enim ad minim veniam, quis nostrud exercitation ullamco laboris nisi ut aliquip ex ea commodo.</p>
    <a class="btn btn-blue" href="#">READ MORE</a>
  </div>
</section>

<section class="learning">
  <h2 class="section-title">Personalisation improves a child's<br><span class="green">learning ability and motivation</span></h2>
  <p class="learning-text">Personalised books offer the possibility of creating magical and unique moments where the child becomes familiar with reading and begins building passion. Share a truly special and magical time welcoming the hero of your own story.</p>
  <div class="video" role="img" aria-label="Video still of a parent and child reading a storybook">
    <svg class="play" viewBox="0 0 60 60"><circle cx="30" cy="30" r="30" fill="#ec1f27"/><path d="M24 18l18 12-18 12z" fill="#fff"/></svg>
  </div>
</section>

<section class="gallery">
  <h2 class="section-title">Our <span class="green">Gallery</span></h2>
  <div class="gallery-grid">
    <div class="tile" role="img" aria-label="Photo of a child holding a storybook" style="background:#c9b7a0"></div>
    <div class="tile tall" role="img" aria-label="Photo of a mother reading with two children" style="background:linear-gradient(160deg,#e8c9a8,#b98c66)"></div>
    <div class="tile" role="img" aria-label="Photo of a child opening a book" style="background:#bcd3e0"></div>
    <div class="tile" role="img" aria-label="Photo of a personalised book cover" style="background:#9fc2d8"></div>
    <div class="tile" role="img" aria-label="Photo of a girl with a necklace" style="background:#d7a7a0"></div>
    <div class="tile" role="img" aria-label="Photo of a father and child reading" style="background:#c7b590"></div>
    <div class="tile" role="img" aria-label="Photo of a child with a gift book" style="background:#a9bfa0"></div>
  </div>
  <div class="gallery-more"><a class="btn btn-red" href="#">VIEW MORE</a></div>
</section>

<blockquote class="testimonial">
  <p><span class="quote">“</span> Lorem ipsum dolor sit amet, consectetur adipiscing elit, sed do eiusmod tempor incididunt ut labore et dolore magna aliqua. Ut enim ad minim veniam, quis nostrud exercitation ullamco laboris nisi ut aliquip ex ea commodo consequat duis aute irure dolor in reprehenderit in voluptate velit esse. <span class="quote">”</span></p>
  <p class="author">Mara Delling City Name</p>
</blockquote>
<div class="dragon" role="img" aria-label="Illustrated purple dragon mascot"></div>

<svg class="footer-stripes" viewBox="0 0 1200 80" preserveAspectRatio="none">
  <path d="M0 40 Q600 0 1200 30" fill="none" stroke="#ec1f27" stroke-width="5"/>
  <path d="M0 50 Q600 12 1200 42" fill="none" stroke="#9bcb3b" stroke-width="5"/>
  <path d="M0 70 Q600 30 1200 60 V80 H0 Z" fill="#1a78bd"/>
</svg>

<footer class="site-footer">
  <div class="footer-col" style="left:172px;width:200px">
    <h4>Contact</h4>
    <div class="contact-line"><svg width="12" height="14" viewBox="0 0 12 14"><path d="M6 13s5-5 5-8.5a5 5 0 0 0-10 0C1 8 6 13 6 13z" fill="#9bcb3b"/><circle cx="6" cy="4.5" r="1.6" fill="#1a78bd"/></svg><span>12 Willow Lane, Kendal<br>Cumbria LA9 4QT</span></div>
    <div class="contact-line"><svg width="12" height="12" viewBox="0 0 12 12"><rect x="0.5" y="2" width="11" height="8" fill="#9bcb3b"/><path d="M0.5 2l5.5 4.5L11.5 2" fill="none" stroke="#1a78bd"/></svg><span>hello@pebblelanternkids.co.uk</span></div>
    <div class="contact-line"><svg width="12" height="12" viewBox="0 0 12 12"><path d="M2 1l2.5 2.5-1.5 1.5a7 7 0 0 0 4 4l1.5-1.5L11 10l-1.5 1.5C5 11 1 7 0.5 2.5z" fill="#9bcb3b"/></svg><span>+44 1539 555 204</span></div>
    <div class="socials"><span></span><span></span><span></span><span></span></div>
  </div>
  <div class="footer-col" style="left:412px">
    <h4>Links</h4>
    <ul><li>Welcome</li><li>About Us</li><li>Our Blog</li><li>Terms &amp; Conditions</li><li>Our Team</li><li>Our Distributors</li></ul>
  </div>
  <div class="footer-col" style="left:580px">
    <h4>Company</h4>
    <ul><li>About Us</li><li>Product Reviews</li><li>Privacy Policy</li><li>Delivery Info</li><li>Returns</li><li>Site Map</li><li>Careers</li></ul>
  </div>
  <div class="footer-col" style="left:756px">
    <h4>My Account</h4>
    <ul><li>My Account</li><li>Order History</li><li>Wish List</li><li>Gift Cards</li><li>Newsletter</li><li>Help</li></ul>
  </div>
  <div class="footer-brand"><span class="brand-dot"></span><span class="brand-name">Pebble Lantern Kids</span></div>
  <div class="footer-bar">Copyright © 2018 Pebble Lantern Kids · Privacy Policy · Terms &amp; Conditions</div>
</footer>

</body>
</html>
```